Cellar Forge - Make Your Own Wine at Home

We need a Tall Market design for a new commerce website based in Minneapolis call CellarForge. We sell equipment and supplies that enable anyone to make great wines at home. We support one's success as a wine maker with recipes, ingredients and equipment designed to never let you fail. We provide the know-how you need with step-by-step instructions, blogs and video classes. The final design should reflect the established Cellar Forge product style as evidenced in the photos. It should appeal to both men and women "makers" who tend to be well educated and technical (designers, engineers, chemists, etc.) It should integrate commerce seamlessly with the learning community in a single site. It should give you confidence that "you can do this well" and "impress your friends" with the wine you made at home.

In order to understand the product line, see

http://www.quillbarrel.com/shop/winemaking

http://www.harrowgoods.com/winemaking-equipment.html
http://www.harrowgoods.com/winemaking-ingredients.html

http://www.plovanti.com/

The deliverables will include psd files for home page, category page, product page and any connect, learn, video and or blog pages you propose as part of the UX/UI.

Target Market(s)

People who make wine, people interested in edible crafts including home brewing and distilling, cheesemaking, coffee roasting, baking, etc. People who love wine and craft beer but did not realize they could make their own.

Industry/Entity Type

Call

Font styles to use
Sans Serif

Requirements
Must have
• Project must reflect best practices in UX and UI design. It must anticipate responsive design application for multiple viewing devices. It must reflect Tall Market advantages and constraints.
Nice to have
• It should be personality driven (http://www.harrowgoods.com/ned-follansby/) but personable and approachable. Winemaking tends to be a community of like minded individuals seeking or sharing experience, technique and success. Navigation should be simple and intuitive (http://www.jarnoddle.co.uk). It should be responsive to the questions of "where is it" (site search), "what do you think about" (reviews), "do you know" (questions and answers).
Should not have
• This should not be whimsical or playful. Making good beer or wine requires discipline -- nobody is proud of a bad batch. It should not be disorganized. It should not reflect confusion as to style (too many colors, fonts or other design elements).

```html
<!DOCTYPE html>
<html lang="en">
<head>
<meta charset="utf-8">
<title>CellarForge – Make Your Own Wine at Home</title>
<link href="https://fonts.googleapis.com/css2?family=Open+Sans:wght@400;600;700&family=Gabriela&display=swap" rel="stylesheet">
<style>
:root{
  --page:#f4f3ef;
  --topbar:#e4e3df;
  --red:#d0303a;
  --red-dark:#b32530;
  --ink:#2d2d2d;
  --muted:#777;
  --mauve:#b58a96;
  --card:#ffffff;
  --card-edge:#e6e5e1;
  --photo-bg:#efede8;
  --teal-band:#bfe3e3;
  --teal-foot:#c8ebeb;
  --teal-line:#9fcfcf;
  --orange:#f7a11a;
  --social:#1f5fa8;
}
*{box-sizing:border-box;margin:0;padding:0}
html,body{width:800px;height:1200px;overflow:hidden}
body{position:relative;background:var(--page);font-family:"Open Sans",Arial,sans-serif;color:var(--ink)}
a{color:inherit;text-decoration:none}
ul{list-style:none}

.topbar{position:absolute;left:0;top:0;width:800px;height:21px;background:var(--topbar);font-size:7px;color:#666}
.topbar ul{position:absolute;right:108px;top:6px;display:flex;gap:14px}

.brand{position:absolute;left:120px;top:46px;display:flex;align-items:center;gap:8px}
.brand-dot{width:34px;height:34px;border-radius:50%;background:var(--red)}
.brand-name{font-size:32px;font-weight:600;color:var(--ink);letter-spacing:-.3px;line-height:40px}

.search{position:absolute;left:536px;top:48px;width:153px;height:19px;border-radius:10px;background:linear-gradient(#e2e2e0,#f2f2f0);border:1px solid #d4d4d0}
.search svg{position:absolute;right:7px;top:3px}
.callout{position:absolute;left:540px;top:73px;font-size:10px;color:#888}
.callout strong{color:#555;font-weight:600}

.mainnav{position:absolute;left:107px;top:100px;width:588px;height:23px;background:var(--red);display:flex;border-bottom:2px solid var(--red-dark)}
.mainnav a{display:flex;align-items:center;justify-content:center;color:#fff;font-size:8px;white-space:nowrap;border-right:1px solid rgba(255,255,255,.35)}
.mainnav a:last-child{border-right:none}

.hero{position:absolute;left:107px;top:139px;width:588px;height:224px;border:1px solid #d8d7d2;background:#fff;padding:4px}
.hero-photo{width:100%;height:100%;
  background:
    radial-gradient(ellipse 70px 45px at 150px 150px,rgba(196,200,90,.9),rgba(196,200,90,0)),
    linear-gradient(90deg,rgba(38,24,14,.95) 0%,rgba(70,44,22,.9) 14%,rgba(120,80,40,.55) 27%,rgba(120,80,40,0) 40%),
    linear-gradient(180deg,#c98a38 0%,#e5b865 14%,#a7923f 26%,#6f8a36 40%,#4f6f26 62%,#3d5a1f 82%,#34501c 100%)}
.hero-caption{position:absolute;left:366px;top:105px;width:214px;height:79px;background:rgba(40,30,15,.55);color:#fff;font-family:"Gabriela",Georgia,serif;font-size:25px;line-height:1.15;text-align:right;padding:8px 14px 0 0}
.hero-dots{position:absolute;left:519px;top:208px;display:flex;gap:5px}
.hero-dots span{width:8px;height:8px;border-radius:50%;background:#ccc}
.hero-dots span:first-child{background:#fff}

.section-label{position:absolute;left:107px;top:377px;width:588px;height:14px;text-align:center}
.section-label::before{content:"";position:absolute;left:0;right:0;top:7px;border-top:1px solid #ddd}
.section-label span{position:relative;background:var(--page);padding:0 6px;font-size:10px;color:#666}
.section-label svg{vertical-align:middle;margin:0 4px}

.product-row{position:absolute;left:109px;width:584px;display:flex;justify-content:space-between}
.row-one{top:408px}
.row-two{top:664px}
.product{width:136px;height:216px;background:var(--card);border:1px solid var(--card-edge);box-shadow:0 0 0 3px #fafaf8;padding:13px 13px 0}
.product-photo{width:110px;height:120px;background-color:var(--photo-bg)}
.product-name{margin-top:4px;font-size:9px;line-height:1.3;color:var(--mauve)}
.product-price{margin-top:2px;font-size:14px;font-weight:700;color:var(--red)}
.add-cart{display:inline-block;margin-top:4px;padding:2px 6px;font-size:7px;border:1px solid #ddd;background:#fff;color:#555}

.photo-press-red{background-image:radial-gradient(ellipse 30px 44px at 55px 62px,#c8302c 0%,#b8513a 45%,rgba(239,237,232,0) 100%)}
.photo-kit-plum{background-image:radial-gradient(ellipse 36px 34px at 52px 60px,#6e2a44 0%,#8a5a5c 50%,rgba(239,237,232,0) 100%)}
.photo-kit-wine{background-image:radial-gradient(ellipse 32px 44px at 55px 62px,#7a1f2a 0%,#5a4838 50%,rgba(239,237,232,0) 100%)}
.photo-kit-violet{background-image:radial-gradient(ellipse 28px 48px at 55px 60px,#3e2e72 0%,#6a5aa0 50%,rgba(239,237,232,0) 100%)}
.photo-press-wood{background-image:radial-gradient(ellipse 28px 50px at 55px 60px,#b8332c 0%,#c08a5a 50%,rgba(239,237,232,0) 100%)}
.photo-kit-navy{background-image:radial-gradient(ellipse 38px 40px at 58px 58px,#1f3a78 0%,#3a5a7a 50%,rgba(239,237,232,0) 100%)}
.photo-pouch{background-image:radial-gradient(ellipse 30px 44px at 55px 60px,#ffffff 0%,#d8d6d0 55%,rgba(239,237,232,0) 100%)}
.photo-kit-indigo{background-image:radial-gradient(ellipse 36px 40px at 55px 60px,#2a2450 0%,#4a3c8a 50%,rgba(239,237,232,0) 100%)}

.row-divider{position:absolute;left:107px;top:644px;width:588px;height:8px;text-align:center}
.row-divider::before{content:"";position:absolute;left:0;right:0;top:4px;border-top:1px solid #ddd}
.row-divider span{position:relative;display:inline-block;width:8px;height:8px;border-radius:50%;background:#f0b9b9;margin:0 1px}

.newsletter{position:absolute;left:0;top:911px;width:800px;height:60px;background:var(--teal-band)}
.newsletter h2{position:absolute;left:144px;top:22px;font-size:12px;font-weight:600;color:#333}
.newsletter .email{position:absolute;left:417px;top:21px;width:172px;height:20px;background:#fff;border:1px solid #cfd;font-size:7px;color:#888;padding:5px 5px}
.newsletter .subscribe{position:absolute;left:593px;top:21px;width:64px;height:20px;background:var(--orange);color:#fff;font-size:9px;font-weight:600;text-align:center;line-height:20px}

.footer{position:absolute;left:0;top:971px;width:800px;height:186px;background:var(--teal-foot);
  background-image:repeating-linear-gradient(45deg,rgba(255,255,255,.18) 0 2px,transparent 2px 6px)}
.footer-col{position:absolute;top:26px;width:120px}
.footer-col h3{display:inline-block;min-width:96px;font-size:11px;font-weight:600;color:#333;white-space:nowrap;padding-bottom:6px;border-bottom:1px solid var(--teal-line);margin-bottom:6px}
.footer-col li{font-size:8px;color:#444;line-height:16.5px;padding-left:8px;position:relative}
.footer-col li::before{content:"";position:absolute;left:1px;top:6px;border-left:3px solid #555;border-top:2px solid transparent;border-bottom:2px solid transparent}
.footer-col p{font-size:8px;color:#444;line-height:12px}
.col-products{left:124px}
.col-harrow{left:276px}
.col-service{left:428px}
.col-connect{left:578px}
.social{display:flex;gap:5px;margin-top:10px}
.social span{width:21px;height:21px;border-radius:50%;background:var(--social);border:2px solid #fff}

.bottombar{position:absolute;left:0;top:1157px;width:800px;height:43px;background:var(--page);text-align:center}
.bottom-links{margin-top:16px;font-size:6.5px;color:#333}
.copyright{margin-top:4px;font-size:7px;color:#c4c4c4}
</style>
</head>
<body>

<header>
  <div class="topbar">
    <ul>
      <li>☏ Call Us (123) 456-7890</li>
      <li>Hi Guest Sign In / Create Account</li>
      <li>Gift Certificates</li>
      <li>Wish Lists</li>
      <li>🛒 Nothing in cart</li>
    </ul>
  </div>

  <a class="brand" href="#"><span class="brand-dot"></span><span class="brand-name">CellarForge</span></a>

  <div class="search">
    <svg width="12" height="12" viewBox="0 0 12 12"><circle cx="5" cy="5" r="3.5" fill="none" stroke="#888" stroke-width="1.4"/><line x1="7.5" y1="7.5" x2="11" y2="11" stroke="#888" stroke-width="1.6"/></svg>
  </div>
  <div class="callout">Just a Call Away: <strong>(123) 546:7890</strong></div>

  <nav class="mainnav">
    <a href="#" style="width:98px">WINE EQUIPMENT</a>
    <a href="#" style="width:99px">WINE INGREDIENTS</a>
    <a href="#" style="width:97px">BEER EQUIPMENT</a>
    <a href="#" style="width:112px">BEER INGREDIENTS</a>
    <a href="#" style="width:51px">OTHER</a>
    <a href="#" style="width:52px">Blog</a>
    <a href="#" style="width:79px">Contact Us</a>
  </nav>
</header>

<main>
  <section class="hero">
    <div class="hero-photo" role="img" aria-label="Wine bottle, glass of white wine and green grapes before an oak barrel, with vineyard rows at sunset"></div>
    <div class="hero-caption">Other Red Wine<br>Varieties</div>
    <div class="hero-dots"><span></span><span></span></div>
  </section>

  <div class="section-label"><span><svg width="5" height="7"><path d="M5 0 0 3.5 5 7z" fill="#555"/></svg>Featured Products<svg width="5" height="7"><path d="M0 0 5 3.5 0 7z" fill="#555"/></svg></span></div>

  <div class="product-row row-one">
    <article class="product"><div class="product-photo photo-press-red" role="img" aria-label="Red wooden basket wine press"></div><p class="product-name">Lorem Ipsum is simply dummy</p><p class="product-price">$112.00</p><a class="add-cart" href="#">Add to cart</a></article>
    <article class="product"><div class="product-photo photo-kit-plum" role="img" aria-label="Boxed wine ingredient kit"></div><p class="product-name">Lorem Ipsum is simply dummy</p><p class="product-price">$112.00</p><a class="add-cart" href="#">Add to cart</a></article>
    <article class="product"><div class="product-photo photo-kit-wine" role="img" aria-label="Red wine kit box"></div><p class="product-name">Lorem Ipsum is simply dummy</p><p class="product-price">$112.00</p><a class="add-cart" href="#">Add to cart</a></article>
    <article class="product"><div class="product-photo photo-kit-violet" role="img" aria-label="Purple wine kit box"></div><p class="product-name">Lorem Ipsum is simply dummy</p><p class="product-price">$112.00</p><a class="add-cart" href="#">Add to cart</a></article>
  </div>

  <div class="row-divider"><span></span><span></span></div>

  <div class="product-row row-two">
    <article class="product"><div class="product-photo photo-press-wood" role="img" aria-label="Red and wood upright wine press"></div><p class="product-name">Lorem Ipsum is simply dummy</p><p class="product-price">$112.00</p><a class="add-cart" href="#">Add to cart</a></article>
    <article class="product"><div class="product-photo photo-kit-navy" role="img" aria-label="Blue wine kit box with a glass of red wine"></div><p class="product-name">Lorem Ipsum is simply dummy</p><p class="product-price">$112.00</p><a class="add-cart" href="#">Add to cart</a></article>
    <article class="product"><div class="product-photo photo-pouch" role="img" aria-label="Sealed pouch of winemaking ingredients"></div><p class="product-name">Lorem Ipsum is simply dummy</p><p class="product-price">$112.00</p><a class="add-cart" href="#">Add to cart</a></article>
    <article class="product"><div class="product-photo photo-kit-indigo" role="img" aria-label="Dark purple wine kit box"></div><p class="product-name">Lorem Ipsum is simply dummy</p><p class="product-price">$112.00</p><a class="add-cart" href="#">Add to cart</a></article>
  </div>
</main>

<section class="newsletter">
  <h2>Sign Up For Our Newsletter</h2>
  <div class="email">Enter your email address</div>
  <a class="subscribe" href="#">Subscribe</a>
</section>

<footer class="footer">
  <div class="footer-col col-products"><h3>PRODUCTS</h3><ul><li>Brewing Equipment</li><li>Brewing Ingredients</li><li>Kegging</li><li>Wine Equipment</li><li>Wine Ingredients</li></ul></div>
  <div class="footer-col col-harrow"><h3>HARROW INFO</h3><ul><li>Brewing Equipment</li><li>Brewing Ingredients</li><li>Kegging</li><li>Wine Equipment</li><li>Wine Ingredients</li></ul></div>
  <div class="footer-col col-service"><h3>CUSTOMER SERVICE</h3><ul><li>Order Status</li><li>Customer Service</li><li>Email Us</li><li>Returns</li><li>My Account</li></ul></div>
  <div class="footer-col col-connect"><h3>GET CONNECTED</h3><p>Phone: 1234567890</p><p>Email:</p><p>Address:</p><div class="social"><span aria-label="Social profile"></span><span aria-label="Social profile"></span><span aria-label="Social profile"></span></div></div>
</footer>

<div class="bottombar">
  <p class="bottom-links">WINE EQUIPMENT | WINE INGREDIENTS | BEER EQUIPMENT | BEER INGREDIENTS | OTHER | RESOURCES &amp; GUIDES | Blog</p>
  <p class="copyright">Copyright · All rights reserved</p>
</div>

</body>
</html>
```